Bright Arch Group business card

Bright Arch Group is the parent company of Bright Arch Building, Bright Arch Plumbing and Bright Arch Renovating. We require a sophisticated business card that covers all aspects of the building and plumbing space without using told or construction items.

Industry/Entity Type

Construction Company

Contact Information for Business Card

Warrick Hadley
Director
0455921834
warrick@brightarch.com.au
Www.brightarch.com.au

Font styles to use
Serif
Sans Serif

Colors
3176b5
ffce3e
0692cd
34a7d8
fbee3e
faa54b

Requirements
Must have
• Logo on front
• Logo and details on rear.
Nice to have
• Maybe water mark or shadow effect with logo
Should not have
• Tools or any construction associated items

```html
<!DOCTYPE html>
<html lang="en">
<head>
<meta charset="utf-8">
<title>Bright Arch Group business card</title>
<link rel="stylesheet" href="https://fonts.googleapis.com/css2?family=Open+Sans:wght@300;400;600&display=swap">
<style>
  :root {
    --bg: #d9d6d2;
    --card: #1b1b1c;
    --card-edge: #262627;
    --accent: #f7931e;
    --light: #f2f2f2;
    --muted: #8d8d8d;
    --divider: #2c2c2d;
  }
  * { margin: 0; padding: 0; box-sizing: border-box; }
  html, body {
    width: 1200px;
    height: 900px;
    overflow: hidden;
    background: var(--bg);
    font-family: "Open Sans", Arial, sans-serif;
  }
  .canvas {
    position: relative;
    width: 1200px;
    height: 900px;
    display: flex;
    align-items: center;
    justify-content: center;
    gap: 40px;
  }
  .card {
    position: relative;
    width: 540px;
    height: 310px;
    background: var(--card);
    border: 1px solid var(--card-edge);
    border-radius: 3px;
    box-shadow: 0 10px 24px rgba(0, 0, 0, 0.25);
    color: var(--light);
  }
  .wordmark {
    display: flex;
    align-items: center;
    gap: 12px;
    color: var(--light);
    font-weight: 300;
    text-transform: uppercase;
    letter-spacing: 0.22em;
    white-space: nowrap;
  }
  .wordmark__dot {
    width: 14px;
    height: 14px;
    border-radius: 50%;
    background: var(--accent);
    flex: none;
  }

  /* Details side */
  .card--details { display: flex; }
  .card--details .brand-panel {
    width: 245px;
    display: flex;
    align-items: center;
    justify-content: center;
    border-right: 1px solid var(--divider);
  }
  .card--details .wordmark { font-size: 15px; letter-spacing: 0.16em; }
  .contact-panel {
    flex: 1;
    padding: 78px 0 0 28px;
  }
  .contact-panel__name {
    color: var(--accent);
    font-weight: 600;
    font-size: 16px;
  }
  .contact-panel__role {
    font-size: 12px;
    margin-top: 1px;
  }
  .contact-list {
    list-style: none;
    margin-top: 30px;
    font-size: 13px;
    line-height: 1.6;
  }
  .contact-list li { display: flex; align-items: center; gap: 10px; }
  .contact-list svg { width: 11px; height: 11px; fill: var(--accent); flex: none; }

  /* Front side */
  .card--front {
    display: flex;
    flex-direction: column;
    align-items: center;
    justify-content: center;
    gap: 34px;
  }
  .card--front .wordmark { font-size: 26px; }
  .services {
    color: var(--muted);
    font-size: 15px;
    letter-spacing: 0.01em;
  }
</style>
</head>
<body>
<main class="canvas">
  <section class="card card--details" aria-label="Business card, contact side">
    <div class="brand-panel">
      <div class="wordmark"><span class="wordmark__dot"></span>Bright Arch Group</div>
    </div>
    <div class="contact-panel">
      <p class="contact-panel__name">Warrick Hadley</p>
      <p class="contact-panel__role">Director</p>
      <ul class="contact-list">
        <li>
          <svg viewBox="0 0 24 24" aria-hidden="true"><path d="M6.6 10.8a15 15 0 0 0 6.6 6.6l2.2-2.2c.3-.3.7-.4 1-.2 1.1.4 2.3.6 3.6.6.6 0 1 .4 1 1V20c0 .6-.4 1-1 1A17 17 0 0 1 3 4c0-.6.4-1 1-1h3.5c.6 0 1 .4 1 1 0 1.3.2 2.5.6 3.6.1.3 0 .7-.2 1z"/></svg>
          0455921834
        </li>
        <li>
          <svg viewBox="0 0 24 24" aria-hidden="true"><path d="M2 5h20v14H2z M2 5l10 8 10-8" /></svg>
          warrick@brightarch.com.au
        </li>
        <li>
          <svg viewBox="0 0 24 24" aria-hidden="true"><circle cx="12" cy="12" r="10"/></svg>
          Www.brightarch.com.au
        </li>
      </ul>
    </div>
  </section>

  <section class="card card--front" aria-label="Business card, brand side">
    <div class="wordmark"><span class="wordmark__dot"></span>Bright Arch Group</div>
    <p class="services">Building | Renovating | Plumbing</p>
  </section>
</main>
</body>
</html>
```